Industrial Project Sign

We need an eye catching (but professional) industrial project sign that will be very large (roughly 12' high x 18' wide). This sign will be highly visible from the adjacent high speed highway.

* The following needs to be at the bottom of the signage: Logo (uploaded), Name (Halvern Land Holdings, Inc.) (uploaded) and phone number (555)739-2864

*Name of Project - "Marrowfield Logistics Park"

* Text items
Land for Sale
Build to Suit
Zoning: Industrial (G I & L I)

* Interesting background that is eye catching

Good morning all,

We are considering all designers options as we go and are waiting for the final designs to come in by the 4th so that we can give each one a good look.   If you have any new designs, questions, further design options or any tweeks you want to do to current designs, please do so at this time.

Thanks to all of you for your submissions.

Industrial

```html
<!DOCTYPE html>
<html lang="en">
<head>
<meta charset="utf-8">
<title>Marrowfield Logistics Park – Project Sign</title>
<link rel="stylesheet" href="https://fonts.googleapis.com/css2?family=Open+Sans:wght@400;600;700;800&display=swap">
<style>
  :root {
    --sign-bg: #e6e7e8;
    --ink: #111111;
    --maroon: #6b1117;
    --slate: #6d6e71;
    --muted: #58595b;
    --white: #ffffff;
  }
  * { margin: 0; padding: 0; box-sizing: border-box; }
  html, body { width: 1200px; height: 800px; overflow: hidden; }
  body { background: var(--sign-bg); font-family: "Open Sans", Arial, sans-serif; }
  .sign { position: relative; width: 1200px; height: 800px; background: var(--sign-bg); }

  .project-title {
    position: absolute; top: 14px; left: 0; width: 100%;
    text-align: center; font-weight: 800; font-size: 57px; letter-spacing: 1px;
    color: var(--ink); line-height: 72px;
  }
  .dot-rule { position: absolute; left: 82px; width: 1046px; height: 14px; }
  .dot-rule--top { top: 89px; }
  .dot-rule--bottom { top: 705px; }

  .offer-band { position: absolute; top: 130px; left: 0; width: 1200px; height: 86px; }
  .offer-band svg { position: absolute; inset: 0; }
  .offer { position: absolute; top: 0; line-height: 86px; color: var(--white);
           font-weight: 800; font-size: 60px; letter-spacing: 1px; }
  .offer--sale { left: 32px; }
  .offer--build { left: 664px; }

  .site-photo {
    position: absolute; top: 216px; left: 0; width: 1200px; height: 216px;
    background: linear-gradient(90deg, #d9d5cc 0%, #d69a3a 25%, #c98a30 50%, #e0a64a 70%, #cfcac0 100%);
  }

  .zoning-band {
    position: absolute; top: 432px; left: 0; width: 1200px; height: 84px;
    background: var(--slate); color: var(--white); text-align: center;
    font-weight: 800; font-size: 58px; line-height: 84px; letter-spacing: 1px;
  }

  .brand-mark { position: absolute; top: 548px; left: 322px; width: 108px; height: 108px; background: var(--maroon); }
  .company-name {
    position: absolute; top: 580px; left: 476px; font-weight: 600; font-size: 25px;
    color: var(--muted); line-height: 34px;
  }
  .name-rule { position: absolute; top: 618px; left: 470px; width: 452px; height: 3px; background: var(--maroon); }
  .company-phone {
    position: absolute; top: 618px; left: 470px; font-weight: 700; font-size: 58px;
    color: var(--ink); line-height: 72px; letter-spacing: 1px;
  }

  .web-address {
    position: absolute; top: 728px; left: 0; width: 100%; text-align: center;
    font-weight: 800; font-size: 49px; line-height: 62px; color: var(--slate);
  }
  .web-address .domain { color: var(--maroon); }
</style>
</head>
<body>
<main class="sign">
  <h1 class="project-title">MARROWFIELD LOGISTICS PARK</h1>

  <svg class="dot-rule dot-rule--top" viewBox="0 0 1046 14" aria-hidden="true">
    <defs>
      <pattern id="dotPattern" width="34" height="14" patternUnits="userSpaceOnUse">
        <circle cx="7" cy="7" r="4.5" fill="#6b1117"/>
        <circle cx="24" cy="7" r="4.5" fill="#6d6e71"/>
      </pattern>
    </defs>
    <rect width="1046" height="14" fill="url(#dotPattern)"/>
  </svg>

  <div class="offer-band">
    <svg width="1200" height="86" viewBox="0 0 1200 86" aria-hidden="true">
      <rect width="1200" height="86" fill="#111111"/>
      <polygon points="0,0 652,0 610,86 0,86" fill="#6b1117"/>
    </svg>
    <span class="offer offer--sale">LAND FOR SALE</span>
    <span class="offer offer--build">BUILD TO SUIT</span>
  </div>

  <div class="site-photo" role="img" aria-label="Photo of a smiling construction worker in a white hard hat in front of a crew in yellow and white hard hats and orange heavy machinery"></div>

  <div class="zoning-band">ZONING: INDUSTRIAL (G I &amp; L I)</div>

  <div class="brand-mark" aria-hidden="true"></div>
  <p class="company-name">Halvern Land Holdings, Inc.</p>
  <div class="name-rule"></div>
  <p class="company-phone">(555)739-2864</p>

  <svg class="dot-rule dot-rule--bottom" viewBox="0 0 1046 14" aria-hidden="true">
    <rect width="1046" height="14" fill="url(#dotPattern)"/>
  </svg>

  <p class="web-address">WWW.<span class="domain">HALVERNLANDHOLDINGS</span>.COM</p>
</main>
</body>
</html>
```